I would like to modify/update my 2 step login screen

I want a more modern looking login page for our document imaging application. I need to keep all of the same elements and buttons that currently exist. The first 2 screens are the login. The 3rd is a screenshot of the actual application home page.

```html
<!DOCTYPE html>
<html lang="en">
<head>
<meta charset="utf-8">
<title>KSS Login</title>
<link rel="stylesheet" href="https://fonts.googleapis.com/css2?family=Montserrat:wght@400;500;600;700&display=swap">
<style>
  :root {
    --ink: #111111;
    --muted: #3a3a3a;
    --line: #bdbdbd;
    --green: #4caf50;
    --green-dark: #389a38;
    --green-light: #85cd85;
    --card: #ffffff;
    --bg-a: #e4e7ea;
    --bg-b: #f7f8f9;
  }
  * { box-sizing: border-box; margin: 0; padding: 0; }
  html, body { width: 1200px; height: 749px; overflow: hidden; }
  body {
    position: relative;
    font-family: "Montserrat", sans-serif;
    color: var(--ink);
    background:
      radial-gradient(ellipse at 50% 45%, var(--bg-b) 0%, rgba(247,248,249,0) 60%),
      linear-gradient(125deg, var(--bg-a) 0%, var(--bg-b) 45%, var(--bg-a) 100%);
  }
  .brand {
    position: absolute; top: 66px; left: 0; width: 1200px;
    text-align: center; font-weight: 700; font-size: 26px; letter-spacing: 1px;
    color: var(--ink);
  }
  .corner { position: absolute; border-color: var(--green); border-style: solid; }
  .corner--top { left: 300px; top: 157px; width: 118px; height: 98px; border-width: 6px 0 0 6px; border-radius: 2px; }
  .corner--bottom { left: 766px; top: 491px; width: 118px; height: 89px; border-width: 0 6px 6px 0; border-radius: 2px; }
  .card {
    position: absolute; left: 306px; top: 163px; width: 571px; height: 410px;
    background: var(--card);
    box-shadow: 0 10px 40px rgba(0,0,0,0.06);
  }
  .card__title {
    position: absolute; top: 30px; width: 100%; text-align: center;
    font-size: 28px; font-weight: 500; letter-spacing: 0.5px;
  }
  .card__rule { position: absolute; left: 249px; top: 70px; }
  .field {
    position: absolute; left: 59px; top: 101px; width: 454px; height: 51px;
    border: 1px solid #a9a9a9; border-radius: 2px;
    display: flex; align-items: center; padding-left: 17px; gap: 11px;
    font-size: 14px; color: var(--muted);
  }
  .btn-primary {
    position: absolute; left: 59px; top: 161px; width: 454px; height: 51px;
    border: 0; border-radius: 2px;
    background: linear-gradient(90deg, var(--green-dark), var(--green-light));
    color: #fff; font-family: inherit; font-weight: 700; font-size: 14px;
    display: flex; align-items: center; justify-content: center; gap: 8px;
  }
  .divider {
    position: absolute; left: 62px; top: 239px; width: 446px;
    display: flex; align-items: center; gap: 13px; font-size: 13px; color: var(--muted);
  }
  .divider::before, .divider::after { content: ""; flex: 1; height: 1px; background: var(--line); }
  .alt-title {
    position: absolute; top: 280px; width: 100%; text-align: center;
    font-size: 13px; font-weight: 700;
  }
  .providers { position: absolute; top: 313px; left: 186px; display: flex; gap: 33px; }
  .provider {
    width: 46px; height: 46px; border-radius: 50%; background: #fff;
    box-shadow: 0 4px 14px rgba(0,0,0,0.12);
    display: flex; align-items: center; justify-content: center;
    font-size: 8px; font-weight: 600; color: var(--ink);
  }
  .footer {
    position: absolute; left: 0; top: 684px; width: 1200px; height: 65px;
    border-top: 1px solid #c9c9c9;
    text-align: center; padding-top: 22px; font-size: 15px; color: #222;
  }
</style>
</head>
<body>
  <div class="brand">KEYSTONE SYSTEMS</div>

  <div class="corner corner--top"></div>
  <div class="corner corner--bottom"></div>

  <main class="card">
    <h1 class="card__title">KSS LOGIN</h1>
    <svg class="card__rule" width="80" height="5" viewBox="0 0 80 5" aria-hidden="true">
      <rect x="0" y="0" width="42" height="4" fill="#111"/>
      <rect x="46" y="0" width="5" height="4" fill="#111"/>
      <rect x="55" y="0" width="5" height="4" fill="#111"/>
      <rect x="64" y="0" width="5" height="4" fill="#111"/>
      <rect x="73" y="0" width="4" height="4" fill="#111"/>
    </svg>

    <label class="field">
      <svg width="16" height="16" viewBox="0 0 16 16" aria-hidden="true">
        <circle cx="8" cy="8" r="7.5" fill="#b9b9b9"/>
        <g fill="none" stroke="#fff" stroke-width="0.9">
          <ellipse cx="8" cy="8" rx="3.2" ry="7.5"/>
          <line x1="8" y1="0.5" x2="8" y2="15.5"/>
          <line x1="0.5" y1="8" x2="15.5" y2="8"/>
          <line x1="2" y1="4.3" x2="14" y2="4.3"/>
          <line x1="2" y1="11.7" x2="14" y2="11.7"/>
        </g>
      </svg>
      <span>Database</span>
    </label>

    <button class="btn-primary">
      LOGIN WITH MYKSVIEW
      <svg width="16" height="14" viewBox="0 0 16 14" aria-hidden="true">
        <path d="M1 7h13M8.5 1.5 14 7l-5.5 5.5" fill="none" stroke="#fff" stroke-width="2" stroke-linecap="round" stroke-linejoin="round"/>
      </svg>
    </button>

    <div class="divider">Or</div>

    <div class="alt-title">LOG IN WITH</div>
    <div class="providers">
      <div class="provider">Gleam</div>
      <div class="provider">Mosaic</div>
      <div class="provider">Onekey</div>
    </div>
  </main>

  <footer class="footer">© 2024 Keystone System. All Rights Reserved</footer>
</body>
</html>
```